Venneputt.dk - FriendPutt

I need a design for a WordPress site that serves to inform and present the national golfchampionship for colleagues in Denmark. The sites need to be visual stuninng or big, and it doesnt have a lot of pages. Maybe 5-6 regular text pages and not a lot of navigation. It should be a simple and powerfull site.

The sites need to present and sell the tournament, and have a clear call to action button "Sign up" (Tilmeld) and resultscoring.

If you can make a logo and visual ID for the tournament as well that would be a bonus.

Target Market(s)

Golfers

Logo Text

Venneputt

Number of Pages Required

3 page

Requirements
Must have
• A frontpage
• Button 1 - Tilmeld (danish for sign up)
• Button 2 - Resultater (results)
Nice to have
• Logo
• A style we can use offline as well

```html
<!DOCTYPE html>
<html lang="da">
<head>
<meta charset="utf-8">
<title>Venneputt 2015</title>
<link href="https://fonts.googleapis.com/css2?family=Roboto:wght@400;500;700&family=Roboto+Condensed:wght@400;700&display=swap" rel="stylesheet">
<style>
:root{
  --green:#0b8a4c;
  --blue:#1a7dc0;
  --red:#c8202f;
  --yellow:#d7a418;
  --navy:#10294c;
  --sky:#3ea0d8;
  --ink:#1e1e1e;
  --text:#333;
  --line:#dcdcdc;
  --panel:#efefef;
  --footer:#222;
  --social-a:#3b5a9a;
  --social-b:#2aa3df;
  --social-c:#dd4b39;
}
*{box-sizing:border-box;margin:0;padding:0}
html,body{width:1200px;height:2416px;overflow:hidden;background:#fff}
body{font-family:"Roboto",Arial,sans-serif;color:var(--text);font-size:13px;position:relative}
.wrap{position:absolute;left:151px;width:898px}

/* header */
.brand{top:14px;height:100px;display:flex;align-items:center;gap:14px}
.brand-dot{width:84px;height:84px;border-radius:50%;background:var(--blue)}
.brand-name{font-family:"Roboto Condensed",sans-serif;font-weight:700;font-size:30px;line-height:1.05;color:var(--ink);letter-spacing:1px;width:240px}
.tools{position:absolute;right:0;top:0;display:flex;flex-direction:column;align-items:flex-end;gap:14px}
.tools-row{display:flex;gap:8px}
.search{display:flex;height:35px}
.search span{width:172px;border:1px solid var(--line);padding:9px 10px;color:#aaa;font-size:12px}
.search b{width:35px;background:var(--ink);display:flex;align-items:center;justify-content:center}
.login{width:106px;height:35px;background:var(--red);color:#fff;display:flex;align-items:center;justify-content:center;gap:8px;font-weight:500;font-size:13px}
.cta{height:48px;display:flex;align-items:center;justify-content:center;gap:10px;color:#fff;font-weight:700;font-size:16px;letter-spacing:1px}
.cta.signup{width:148px;background:var(--green)}
.cta.results{width:181px;background:var(--blue)}
.nav-main{top:124px;display:flex;gap:4px;height:39px}
.nav-main a{background:var(--ink);color:#fff;font-size:12px;display:flex;align-items:center;justify-content:center;text-decoration:none;flex:auto;padding:0 8px}
.nav-sub{top:167px;display:flex;gap:4px;height:44px}
.nav-sub a{flex:1;color:#fff;font-size:15px;display:flex;align-items:center;justify-content:center;text-decoration:none}

/* hero */
.hero{position:absolute;left:0;top:216px;width:1200px;height:430px;background:linear-gradient(180deg,#6f7d86 0%,#a9a79a 45%,#c9b9a0 75%,#8a8675 100%)}
.hero-title{position:absolute;left:151px;top:142px;font-family:"Roboto Condensed",sans-serif;font-weight:700;font-size:31px;color:#fff}
.finder{position:absolute;left:216px;top:304px;width:770px;height:68px;background:#fff;display:flex;align-items:center;gap:8px;padding:0 17px}
.finder label{font-size:14px;color:var(--ink);width:185px;line-height:1.25;text-transform:uppercase}
.finder .field{height:36px;border:1px solid #ccc;display:flex;align-items:center;justify-content:space-between;padding:0 10px;font-size:12px;color:var(--ink)}
.finder .go{width:68px;height:36px;background:var(--blue);color:#fff;font-weight:700;display:flex;align-items:center;justify-content:center;font-size:13px}
.dots{position:absolute;top:394px;left:0;width:1200px;display:flex;justify-content:center;gap:20px;align-items:center}
.dots i{width:12px;height:12px;border-radius:50%;background:#fff}
.dots i.on{width:17px;height:17px;background:none;border:2px solid #fff}

/* columns */
.col-left{position:absolute;left:151px;top:659px;width:554px}
.col-right{position:absolute;left:716px;top:659px;width:332px}
.event-head{display:flex;height:187px;gap:11px}
.event-intro{width:357px;background:var(--ink);color:#fff;padding:30px 28px}
.event-date{font-family:"Roboto Condensed",sans-serif;font-weight:700;font-size:22px;margin-bottom:12px}
.event-date em{font-style:normal;color:var(--red)}
.event-lead{font-family:"Roboto Condensed",sans-serif;font-size:20px;line-height:1.5}
.event-facts{flex:1;background:var(--red);color:#fff;padding:22px 18px;font-size:12.5px;line-height:1.55}
.event-facts h4{font-weight:400;font-size:13px;display:flex;gap:8px;align-items:center}
.event-facts p{font-weight:700;margin-bottom:16px}
.banner{margin-top:6px;height:122px;background:linear-gradient(90deg,#9aa39c 0%,#4f8f2f 30%,#3f7f25 100%);position:relative}
.banner p{position:absolute;right:40px;top:20px;width:330px;text-align:center;font-family:"Roboto Condensed",sans-serif;font-weight:700;font-size:16px;line-height:1.3;color:#fff;text-transform:uppercase}
.promo{margin-top:6px;height:197px;background:#a9d3ef;position:relative;padding:22px 0 0 22px}
.promo p{color:#fff;font-size:18px;line-height:1.5}
.promo b{font-weight:700}
.promo .art{position:absolute;right:45px;top:14px;width:150px;height:178px;background:linear-gradient(180deg,#c9dbe5,#c5a37a);border-radius:4px}
.price{margin-top:14px;width:203px;height:61px;border:1px solid var(--line);display:flex;align-items:center;gap:14px;padding:0 20px;font-size:14px;line-height:1.3}
.price strong{color:var(--red);font-weight:700}
.card{margin-top:11px;border:1px solid var(--line);padding:14px 18px 14px 52px;position:relative;font-size:13px;line-height:1.45;color:#444}
.card .ic{position:absolute;left:16px;top:16px}
.card h3{font-family:"Roboto Condensed",sans-serif;font-weight:700;font-size:15px;margin-bottom:4px;text-transform:uppercase}
.card p+p{margin-top:10px}
.h-yellow{color:var(--yellow)}.h-green{color:var(--green)}.h-red{color:var(--red)}.h-blue{color:var(--blue)}.h-navy{color:var(--navy)}.h-sky{color:var(--sky)}
.rounds{display:flex;margin-top:14px}
.round{flex:1;text-align:center;border-left:1px solid var(--line);font-size:13px;color:#444}
.round:first-child{border:0}
.round i{display:block;margin:5px auto;width:26px;height:26px;border-radius:50%;color:#fff;font-style:normal;font-weight:700;line-height:26px}
.round b{font-weight:700;font-size:13px}
.prizes{padding-left:22px;margin-top:10px}
.prizes li{margin-bottom:10px;padding-left:4px}
.prizes li:last-child{margin-bottom:2px}
.prizes b{color:var(--green);font-weight:700;font-size:14px}

.box{border:1px solid var(--line);padding:20px 20px}
.box h2{font-family:"Roboto Condensed",sans-serif;font-weight:700;font-size:18px;color:var(--blue);display:flex;gap:12px;align-items:center;text-transform:uppercase;margin-bottom:12px}
.events-box{height:406px}
.events{list-style:none;font-size:12px;color:#333}
.events li{height:27.6px;display:flex;align-items:center;gap:10px}
.events li:before{content:"";border-left:5px solid #555;border-top:4px solid transparent;border-bottom:4px solid transparent}
.info{margin-top:11px;height:377px;background:var(--panel);border:1px solid var(--line)}
.docs{list-style:none}
.docs li{height:52px;border-bottom:1px solid #ccc;display:flex;align-items:center;gap:14px;font-size:13px;font-weight:700;color:var(--ink)}
.docs li:last-child{border:0}
.docs small{font-weight:400;font-size:11px;color:#666}
.chev{width:15px;height:15px;border-radius:50%;background:var(--red);display:inline-flex;align-items:center;justify-content:center}
.video{margin-top:13px;height:267px;background:linear-gradient(180deg,#8fa9c0 0%,#6f8a5a 55%,#4f6f3a 100%);position:relative}
.video .play{position:absolute;left:140px;top:100px;width:54px;height:40px;background:var(--red);border-radius:8px;display:flex;align-items:center;justify-content:center}
.video .bar{position:absolute;left:0;bottom:0;width:100%;height:14px;background:#eee;display:flex;align-items:center;padding:0 8px;gap:8px;font-size:8px;color:#333}
.video .bar i{flex:1;height:4px;background:#bbb}
.contact{margin-top:16px;height:250px;background:#dcdcdc;padding:28px 0 0 66px}
.contact .photo{width:192px;height:88px;background:linear-gradient(90deg,#b08670,#6a4c3c 50%,#b3a290)}
.contact h4{font-family:"Roboto Condensed",sans-serif;font-weight:700;font-size:16px;letter-spacing:1.5px;margin:20px 0 6px;color:var(--ink)}
.contact p{font-size:12px;line-height:1.85;color:#333}
.partners{margin-top:16px;height:222px;border:1px solid var(--line);display:flex;flex-direction:column;align-items:center;padding-top:22px}
.partners small{font-size:11px;color:#333}
.partner-name{font-family:"Roboto",sans-serif;font-weight:500;font-size:19px;color:var(--green);margin-top:2px}
.partner-mark{width:64px;height:64px;border-radius:50%;background:#dfe6ee;margin:18px 0 10px}
.partner-name.alt{color:var(--blue);font-size:28px;margin-top:0}

/* footer */
.footer{position:absolute;left:0;top:2250px;width:1200px;height:166px;background:var(--footer);color:#ddd}
.footer .inner{position:absolute;left:151px;width:898px;top:0;height:166px}
.f-brand{position:absolute;left:0;top:30px;width:92px;height:92px;border-radius:50%;background:var(--blue)}
.f-address{position:absolute;left:122px;top:40px;font-size:12px;line-height:2}
.f-follow{position:absolute;left:398px;top:38px;font-size:12px}
.socials{display:flex;gap:8px;margin-top:14px}
.socials i{width:27px;height:27px}
.f-badge{position:absolute;right:0;top:26px;display:flex;flex-direction:column;align-items:center;gap:6px}
.f-badge i{width:60px;height:50px;border-radius:50%;background:var(--red)}
.f-badge span{font-family:"Roboto",sans-serif;font-weight:700;font-size:24px;color:#fff}
.f-rule{position:absolute;left:0;right:0;top:122px;border-top:1px solid #444}
.f-copy{position:absolute;right:0;top:136px;font-size:11px;color:#bbb}
</style>
</head>
<body>

<header class="wrap brand">
  <div class="brand-dot"></div>
  <div class="brand-name">NORDLYS IDRÆTS&shy;FORBUND</div>
  <div class="tools">
    <div class="tools-row">
      <div class="search"><span>Search</span><b><svg width="14" height="14" viewBox="0 0 14 14"><circle cx="6" cy="6" r="4.5" fill="none" stroke="#fff" stroke-width="2"/><path d="M9.5 9.5 13 13" stroke="#fff" stroke-width="2"/></svg></b></div>
      <div class="login"><svg width="11" height="13" viewBox="0 0 11 13"><rect x="0" y="5" width="11" height="8" fill="#fff"/><path d="M2.5 5V3.5a3 3 0 0 1 6 0V5" fill="none" stroke="#fff" stroke-width="1.6"/></svg>Login</div>
    </div>
    <div class="tools-row">
      <div class="cta signup"><svg width="16" height="16" viewBox="0 0 16 16"><rect x="1" y="3" width="11" height="11" fill="none" stroke="#fff" stroke-width="1.6"/><path d="M6 10 14 2" stroke="#fff" stroke-width="2"/></svg>TILMELD</div>
      <div class="cta results"><svg width="16" height="14" viewBox="0 0 16 14"><rect x="0" y="0" width="16" height="3" fill="#fff"/><rect x="0" y="5.5" width="16" height="3" fill="#fff"/><rect x="0" y="11" width="16" height="3" fill="#fff"/></svg>RESULTATER</div>
    </div>
  </div>
</header>

<nav class="wrap nav-main">
  <a>Om Nordlys Idrætsforbund</a><a>Bliv medlem</a><a>Magasinet NORDLYS</a><a>Find forening</a><a>Pressecenter</a><a>Find person</a><a>Min side</a>
</nav>
<nav class="wrap nav-sub">
  <a style="background:var(--green)">Idræt og motion</a>
  <a style="background:var(--yellow)">Arrangementer og stævner</a>
  <a style="background:var(--red)">Sundhed på arbejdspladsen</a>
  <a style="background:var(--navy)">Foreningsnet</a>
</nav>

<section class="hero" role="img" aria-label="Golfspiller i fuldt sving mod en skyet himmel">
  <h1 class="hero-title">VENNEPUTT 2015</h1>
  <div class="finder">
    <label>Find arrangement/ stævne:</label>
    <div class="field" style="width:172px">Søgeord</div>
    <div class="field" style="width:148px">Vælg Kommune <svg width="9" height="5"><path d="M0 0h9L4.5 5z" fill="#333"/></svg></div>
    <div class="field" style="width:148px">Vælg tidspunkt <svg width="9" height="5"><path d="M0 0h9L4.5 5z" fill="#333"/></svg></div>
    <div class="go">SØG</div>
  </div>
  <div class="dots"><i></i><i class="on"></i><i></i><i></i><i></i></div>
</section>

<main class="col-left">
  <div class="event-head">
    <div class="event-intro">
      <div class="event-date">27. APRIL <em>2015</em></div>
      <p class="event-lead">Danmarks sjoveste venneturnering<br>i golf. Spil mod andre spillere på<br>nye baner.</p>
    </div>
    <div class="event-facts">
      <h4><svg width="12" height="12" viewBox="0 0 12 12"><circle cx="6" cy="6" r="5" fill="none" stroke="#fff" stroke-width="1.4"/><path d="M6 3v3h2.5" fill="none" stroke="#fff" stroke-width="1.4"/></svg>Tidspunkt:</h4>
      <p>maj 2015 kl. 07:00 -<br>18. sep 2015 kl. 21:30</p>
      <h4><svg width="13" height="10" viewBox="0 0 13 10"><rect x="0.7" y="0.7" width="11.6" height="8.6" fill="none" stroke="#fff" stroke-width="1.4"/><path d="M1 1l5.5 4.5L12 1" fill="none" stroke="#fff" stroke-width="1.4"/></svg>Kontakt:</h4>
      <p>Mette Skovgaard, Tlf.<br>40123456</p>
    </div>
  </div>

  <div class="banner" role="img" aria-label="Golfkøller og golfbold på grøn fairway">
    <p>Turneringen afvikles i 2015 for 8. gang. Finalestævnet er i år på Egelund Golfklubs bane på Fyn.</p>
  </div>

  <div class="promo">
    <p>Vær med, og vind rejsegavekort<br>for hele holdet på op til<br><b>kr. 22.000,-</b> som 1. præmie,<br>dog max. <b>kr. 5.500,-</b> pr.<br>deltager, jf.<br>amatørbestemmelserne.</p>
    <div class="art" role="img" aria-label="Indkøbspose med kendte rejsemål og et fly"></div>
  </div>

  <div class="price">
    <svg width="20" height="20" viewBox="0 0 20 20"><path d="M2 10 10 2h8v8l-8 8z" fill="var(--red)"/><circle cx="14.5" cy="5.5" r="1.6" fill="#fff"/></svg>
    <div>PRIS<br><strong>KR. 500,- PR. HOLD.</strong></div>
  </div>

  <div class="card">
    <svg class="ic" width="20" height="16" viewBox="0 0 20 16"><circle cx="6" cy="4" r="3" fill="var(--yellow)"/><circle cx="14" cy="4" r="3" fill="var(--yellow)"/><path d="M0 14a6 5 0 0 1 12 0zM8 14a6 5 0 0 1 12 0z" fill="var(--yellow)"/></svg>
    <h3 class="h-yellow">Deltagere</h3>
    <p>Turneringen er åben for alle klubgolfere med gyldigt golfkort, gyldigt handicap og amatørstatus.</p>
  </div>

  <div class="card">
    <svg class="ic" width="16" height="16" viewBox="0 0 16 16"><path d="M2 1l13 7-13 7z" fill="var(--green)"/></svg>
    <h3 class="h-green">Spilleform</h3>
    <p>Spilleformen er en fourball - high/low hulspilsturnering, hvor 2 spillere fra holdet spiller med 2 spillere fra et andet hold. Læs mere i turneringsbetingelserne, som du finder her på siden.</p>
  </div>

  <div class="card">
    <svg class="ic" width="16" height="16" viewBox="0 0 16 16"><rect x="1" y="2" width="14" height="13" fill="none" stroke="var(--red)" stroke-width="1.6"/><path d="M1 6h14M5 0v4M11 0v4" stroke="var(--red)" stroke-width="1.6"/></svg>
    <h3 class="h-red">Stopdatoer</h3>
    <div class="rounds">
      <div class="round">Runde<i style="background:var(--green)">1</i><b class="h-green">18. maj</b></div>
      <div class="round">Runde<i style="background:var(--yellow)">2</i><b class="h-yellow">8. juni</b></div>
      <div class="round">Runde<i style="background:var(--sky)">3</i><b class="h-sky">29. juni</b></div>
      <div class="round">Runde<i style="background:var(--navy)">4</i><b class="h-navy">17. august</b></div>
      <div class="round">Runde<i style="background:var(--red)">5</i><b class="h-red">7. september</b></div>
    </div>
  </div>

  <div class="card">
    <svg class="ic" width="20" height="18" viewBox="0 0 20 18"><path d="M5 1h10v5a5 5 0 0 1-10 0z" fill="var(--blue)"/><path d="M5 3H1.5a3.5 3.5 0 0 0 4 4M15 3h3.5a3.5 3.5 0 0 1-4 4" fill="none" stroke="var(--blue)" stroke-width="1.5"/><path d="M9 11h2v4H9zM6 15h8v2H6z" fill="var(--blue)"/></svg>
    <h3 class="h-blue">Finalestævne fredag den 18. september 2015</h3>
    <p>Vinderne fra hver pulje kvalificerer sig til at deltage i finalestævnet, som spilles på Egelund Golfklub, Skovbrynet 14, 5400 Egelund fredag den 18 September 2015 kl. 10.00.</p>
    <p>Finalen bliver spillet som stableford four-ball best-ball med 7/8 handicap og med gunstart.</p>
    <p>Finalestævnet spilles af to spillere fra hvert hold. Greenfee og middag betales af Nordlys Idrætsforbund.</p>
  </div>

  <div class="card">
    <svg class="ic" width="22" height="16" viewBox="0 0 22 16"><path d="M11 0l2.3 4.8 5.2.7-3.8 3.6.9 5.2L11 11.8 6.4 14.3l.9-5.2L3.5 5.5l5.2-.7z" fill="var(--navy)"/><path d="M3 6l1 2 2 .3-1.5 1.4.4 2L3 10.8 1.1 11.7l.4-2L0 8.3 2 8z" fill="var(--navy)"/></svg>
    <h3 class="h-navy">Præmier</h3>
    <p>Puljevindernes præmie er deltagelse i finalestævnet.<br>Nordlys Idrætsforbund betaler greenfee, sportsbolle, vand og middag til finalestævnet.</p>
  </div>

  <div class="card">
    <svg class="ic" width="22" height="16" viewBox="0 0 22 16"><path d="M1 3l5 5 5-7 5 7 5-5-2 11H3z" fill="var(--green)"/></svg>
    <h3 class="h-green">Finalepræmier</h3>
    <ol class="prizes">
      <li>præmie: Et rejsegavekort på op til <b>kr.22.000,-</b> pr. hold, dog max. <b>kr.5.500</b> pr. tilmeldt spiller.</li>
      <li>præmie: Et gavekort til golfudstyr på <b>kr.2,000-</b> pr. hold.</li>
      <li>præmie: Et gavekort til golfudstyr på <b>kr.1.000-</b> pr. hold.</li>
    </ol>
  </div>
</main>

<aside class="col-right">
  <div class="box events-box">
    <h2><svg width="16" height="16" viewBox="0 0 16 16"><rect x="1" y="2" width="14" height="13" fill="none" stroke="var(--blue)" stroke-width="1.6"/><path d="M1 6h14M5 0v4M11 0v4" stroke="var(--blue)" stroke-width="1.6"/></svg>Arrangementer og stævner</h2>
    <ul class="events">
      <li>Nordlys Open</li><li>Cykel &amp; Løb Stafetten</li><li>Ekstrem Herretræf</li><li>Fælles Motionsdag 2015</li><li>Adventurerace</li><li>Venneputt</li><li>Vennebold</li><li>Vest Cup Fodbold</li><li>Vest Cup Høvdingebold</li><li>Internetskydning</li><li>Gokart</li><li>Arkiv</li>
    </ul>
  </div>

  <div class="box info">
    <h2><svg width="14" height="17" viewBox="0 0 14 17"><path d="M0 0h9l5 5v12H0z" fill="var(--blue)"/><path d="M3 8h8M3 11h8M3 14h6" stroke="#fff" stroke-width="1.3"/></svg>Mere information</h2>
    <ul class="docs">
      <li><svg width="16" height="18" viewBox="0 0 16 18"><path d="M1 1h9l5 5v11H1z" fill="none" stroke="var(--red)" stroke-width="1.6"/></svg><span>Puljer <small>(PDF, 203 KB)</small></span><i class="chev"><svg width="7" height="5"><path d="M0 0l3.5 4L7 0" fill="none" stroke="#fff" stroke-width="1.5"/></svg></i></li>
      <li><svg width="16" height="18" viewBox="0 0 16 18"><path d="M1 1h9l5 5v11H1z" fill="none" stroke="var(--red)" stroke-width="1.6"/></svg><span>Turneringsplan <small>(PDF, 339 KB)</small></span><i class="chev"><svg width="7" height="5"><path d="M0 0l3.5 4L7 0" fill="none" stroke="#fff" stroke-width="1.5"/></svg></i></li>
      <li><svg width="16" height="18" viewBox="0 0 16 18"><path d="M1 1h9l5 5v11H1z" fill="none" stroke="var(--red)" stroke-width="1.6"/></svg><span>Turneringsbetingelser <small>(PDF, 339 KB)</small></span><i class="chev"><svg width="7" height="5"><path d="M0 0l3.5 4L7 0" fill="none" stroke="#fff" stroke-width="1.5"/></svg></i></li>
      <li><svg width="16" height="18" viewBox="0 0 16 18"><path d="M1 1h9l5 5v11H1z" fill="none" stroke="var(--red)" stroke-width="1.6"/></svg><span>Holdkaptajner <small>(PDF, 339 KB)</small></span><i class="chev"><svg width="7" height="5"><path d="M0 0l3.5 4L7 0" fill="none" stroke="#fff" stroke-width="1.5"/></svg></i></li>
      <li><svg width="16" height="18" viewBox="0 0 16 18"><path d="M1 1h9l5 5v11H1z" fill="none" stroke="var(--red)" stroke-width="1.6"/></svg><span>7_8_handicaptabel <small>(PDF, 339 KB)</small></span><i class="chev"><svg width="7" height="5"><path d="M0 0l3.5 4L7 0" fill="none" stroke="#fff" stroke-width="1.5"/></svg></i></li>
      <li><svg width="16" height="18" viewBox="0 0 16 18"><path d="M1 1h9l5 5v11H1z" fill="none" stroke="var(--red)" stroke-width="1.6"/></svg><span>Ofte stillede spørgsmål <small>(PDF, 339 KB)</small></span><i class="chev"><svg width="7" height="5"><path d="M0 0l3.5 4L7 0" fill="none" stroke="#fff" stroke-width="1.5"/></svg></i></li>
    </ul>
  </div>

  <div class="video" role="img" aria-label="Videoklip med to golfspillere og golfbags på banen">
    <div class="play"><svg width="16" height="18" viewBox="0 0 16 18"><path d="M0 0l16 9-16 9z" fill="#fff"/></svg></div>
    <div class="bar"><span>00:00</span><i></i><span>00:00</span></div>
  </div>

  <div class="contact">
    <div class="photo" role="img" aria-label="Portrætfoto af generalsekretæren"></div>
    <h4>LARS HOLMGAARD</h4>
    <p>Generalsekretær<br>Tlf: 40 55 21 80<br>Mail: lh@nordlysidraet.dk</p>
  </div>

  <div class="partners">
    <small>I samarbejde med:</small>
    <div class="partner-name">FAIRWAY SAMRÅDET</div>
    <div class="partner-mark"></div>
    <div class="partner-name alt">Bølge Rejser</div>
  </div>
</aside>

<footer class="footer">
  <div class="inner">
    <div class="f-brand"></div>
    <div class="f-address">Nordlys Idrætsforbund Havnevej 8<br>5700 Lindby Tlf. 65 10 20 30<br>kontakt@nordlysidraet.dk</div>
    <div class="f-follow">Follow Us On
      <div class="socials">
        <i style="background:var(--social-a)"></i>
        <i style="background:var(--social-b)"></i>
        <i style="background:var(--social-c)"></i>
      </div>
    </div>
    <div class="f-badge"><i></i><span>FGS</span></div>
    <div class="f-rule"></div>
    <div class="f-copy">Copyrights @ 2015 All Rights Reserved</div>
  </div>
</footer>

</body>
</html>
```